RESIDENTIAL CONSTRUCTION

We are a company that specializes in building custom residential homes, the design should also emphasize that quality and service is our priority.

Industry/Entity Type

Construction Company

Contact Information for Business Card

Contact Person: Tobias Kerrigan
Company Address: 243 West 9th St San Jose , Ca 95387
Phone Number : 408-736-2049
Email Address: Stonegatecrafts517@mailbrook.net

Font styles to use
Sans Serif

Colors
ec1f27

Requirements
Must have
• CSLB # 2736159
Nice to have
• needs to have same color as logo i uploaded, we will be printing these on a clear plastic card.

```html
<!DOCTYPE html>
<html lang="en">
<head>
<meta charset="utf-8">
<title>Stonegate General Builders – Business Card</title>
<link href="https://fonts.googleapis.com/css2?family=Roboto:wght@400;700;900&display=swap" rel="stylesheet">
<style>
  :root {
    --backdrop: #8a8a8a;
    --card: #f6f6f6;
    --brand-red: #b0101e;
    --text-grey: #3c3c3c;
    --rule: #c8c8c8;
  }
  * { box-sizing: border-box; margin: 0; padding: 0; }
  html, body {
    width: 1200px;
    height: 904px;
    overflow: hidden;
    background: var(--backdrop);
    font-family: "Roboto", Arial, sans-serif;
  }
  .business-card {
    position: absolute;
    left: 180px;
    top: 212px;
    width: 840px;
    height: 480px;
    background: var(--card);
    box-shadow: 0 18px 40px rgba(0,0,0,0.25);
    display: flex;
    align-items: center;
  }
  .brand {
    width: 470px;
    padding-left: 60px;
    display: flex;
    align-items: center;
    gap: 16px;
  }
  .brand-square {
    width: 46px;
    height: 46px;
    background: var(--brand-red);
    flex: none;
  }
  .brand-name {
    color: var(--brand-red);
    font-weight: 900;
    font-size: 34px;
    line-height: 1.05;
    text-transform: uppercase;
    letter-spacing: 0.5px;
  }
  .divider {
    width: 1px;
    height: 190px;
    background: var(--rule);
  }
  .contact {
    padding-left: 34px;
    color: var(--text-grey);
    font-size: 19px;
    line-height: 1.28;
  }
  .contact-name {
    color: var(--brand-red);
    font-weight: 700;
    font-size: 25px;
    text-transform: uppercase;
    letter-spacing: 0.6px;
    margin-bottom: 6px;
  }
  .contact-address { margin-bottom: 10px; }
  .contact-row {
    display: flex;
    align-items: center;
    gap: 12px;
  }
  .contact-row svg { width: 15px; height: 15px; flex: none; }
</style>
</head>
<body>
  <div class="business-card">
    <div class="brand">
      <div class="brand-square"></div>
      <div class="brand-name">Stonegate<br>General Builders</div>
    </div>
    <div class="divider"></div>
    <div class="contact">
      <div class="contact-name">Tobias Kerrigan</div>
      <div class="contact-address">
        243 West 9th St San Jose<br>
        Ca 95387<br>
        CSLB # 2736159
      </div>
      <div class="contact-row">
        <svg viewBox="0 0 16 16" aria-hidden="true"><path fill="#b0101e" d="M3.6 1.2l2.3 2.9-1.4 1.6c.9 2 2.4 3.6 4.5 4.6l1.6-1.4 2.9 2.3-1.3 2.8C7 13.7 2.3 9 1 3z"/></svg>
        <span>408-736-2049</span>
      </div>
      <div class="contact-row">
        <svg viewBox="0 0 16 16" aria-hidden="true"><rect x="1" y="3" width="14" height="10" fill="#b0101e"/><path d="M1.5 3.5L8 9l6.5-5.5" fill="none" stroke="#f6f6f6" stroke-width="1.3"/></svg>
        <span>Stonegatecrafts517@mailbrook.net</span>
      </div>
      <div class="contact-row">
        <svg viewBox="0 0 16 16" aria-hidden="true"><circle cx="8" cy="8" r="7" fill="#b0101e"/><path d="M1 8h14M8 1c-3 3-3 11 0 14M8 1c3 3 3 11 0 14" fill="none" stroke="#f6f6f6" stroke-width="1"/></svg>
        <span>www.stonegatecrafts.net</span>
      </div>
    </div>
  </div>
</body>
</html>
```